2 page PSD web design

I need a fairly simple website design built in PSD format for a site / blog in the finance niche. My current web address is www.velmarquest.com. Velmar Quest Hub is a site that teaches people how to trade options with a focus on income strategies.

I need a simple homepage built and then another similar template for all other pages including blog posts.

The rough design layout is shown attached excel file. It is similar to www.dorentakessly.com although I don't like the colors on his site at all. My logo is attached also, so the colours should be aligned with my logo.

In the header section, I will be giving away a free ebook called "No-Fluff Manual for Calendar Spreads" so I will need a 2D and 3D book cover designed as well. The design should be aligned with my logo and site design.

Industry/Entity Type

Finance

Requirements
Must have
• Everything is detailed in the excel file, but here is a list of must have items:

My current logo
ebook design and sign up section
under the ebook sign up section, need a big bold heading - "HELPING YOU TRADE IRON CONDORS AND OTHER INCOME STRATEGIES WITHOUT THE BS"
6 sidebar sections as detailed in excel file
Social Proof at top right, on the same line / level as the logo
"home advertise contact" in the top left in small discreet font
Should not have
• Do not want any photos or images on either of the pages

```html
<!DOCTYPE html>
<html lang="en">
<head>
<meta charset="utf-8">
<title>Velmar Quest Hub</title>
<link rel="stylesheet" href="https://fonts.googleapis.com/css2?family=Open+Sans:wght@400;600;700&family=Roboto+Condensed:wght@400;700&family=Tinos&display=swap">
<style>
:root{
  --ink:#1a1a1a;
  --black:#0b0b0b;
  --page-bg:#e9ecef;
  --white:#ffffff;
  --blue:#2b5fb3;
  --blue-deep:#1f4f9e;
  --blue-title:#3d6ea8;
  --side-blue:#5f9fd3;
  --side-blue-dark:#3f83c2;
  --btn-blue:#3a85d6;
  --btn-blue-dark:#2467b8;
  --red:#cc1f1f;
  --grey-text:#333;
  --line:#d9dde2;
}
*{box-sizing:border-box;margin:0;padding:0}
html,body{width:1200px;height:2400px;overflow:hidden}
body{background:var(--page-bg);font-family:"Open Sans",Arial,sans-serif;color:var(--ink);position:relative}
.topbar{position:absolute;left:0;top:0;width:1200px;height:30px;background:var(--black)}
.topbar ul{list-style:none;display:flex;position:absolute;left:139px;top:7px;font-size:12px}
.topbar li{color:#ddd;padding:0 9px;border-left:1px solid #555;line-height:14px}
.topbar li:first-child{border:none;padding-left:0;color:#fff;font-weight:700}
.page{position:absolute;left:99px;top:30px;width:1002px;height:2300px;background:var(--white);box-shadow:0 0 6px rgba(0,0,0,.25)}
.brand{position:absolute;left:120px;top:78px;display:flex;align-items:center;gap:14px}
.brand-dot{width:62px;height:62px;border-radius:50%;background:var(--blue-deep)}
.brand-name{font-size:30px;font-weight:700;color:var(--blue-deep)}
.social-proof{position:absolute;right:133px;top:70px;font-size:19px;color:#444;display:flex;align-items:center;gap:10px}
.count{background:#222;color:#fff;border-radius:8px;padding:1px 10px;font-size:18px}
.social{position:absolute;right:139px;top:123px;display:flex;gap:7px}
.social span{width:32px;height:32px;border-radius:6px;background:#5a7fb8}
.nav{position:absolute;left:91px;top:181px;width:1018px;height:38px;background:linear-gradient(#2a2a2a,#000);display:flex;gap:30px;padding-left:75px;align-items:center;font-size:15px;color:#fff}
.hero{position:absolute;left:109px;top:229px;width:979px;height:371px;background:linear-gradient(#2f6ac4,#1f54a6);overflow:hidden}
.hero-screen{position:absolute;left:54px;top:27px;width:406px;height:300px;background:linear-gradient(135deg,#c9d6e4,#7d8fa8);border-radius:10px}
.dots{position:absolute;left:32px;top:334px;display:flex;gap:10px}
.dots span{width:10px;height:10px;border-radius:50%;background:#fff}
.hero h2{position:absolute;left:487px;top:54px;width:480px;font-weight:400;color:#fff;font-size:22px;line-height:31px}
.hero ul{list-style:none;position:absolute;left:487px;top:140px;width:260px;color:#fff;font-size:14px;line-height:19px}
.hero li{padding-left:32px;position:relative;margin-bottom:22px}
.hero li svg{position:absolute;left:0;top:2px}
.ebook{position:absolute;left:790px;top:118px;width:110px;height:170px;background:linear-gradient(90deg,#c9ced6,#f4f5f7);border-radius:4px}
.instant{position:absolute;left:710px;top:300px;width:200px;height:46px;border-radius:6px;background:linear-gradient(#fff,#dfe6ef);color:var(--blue-deep);font-size:20px;font-weight:600;display:flex;align-items:center;justify-content:center;border:2px solid #cfd9e6}
.tagline{position:absolute;left:112px;top:618px;width:976px;height:83px;border-radius:8px;background:linear-gradient(#2b2b2b,#000);color:#fff;font-family:"Tinos",serif;font-weight:400;font-size:29px;line-height:36px;text-align:center;padding-top:6px}
.section-head{position:absolute;left:128px;width:653px;height:44px;border-radius:4px;background:linear-gradient(#7d9cc8,#3e65a1);color:#fff;font-family:"Roboto Condensed",sans-serif;font-weight:400;font-size:21px;padding:8px 20px}
.post-list{position:absolute;left:128px;width:653px;border:1px solid var(--line);background:#fff}
.post{height:237px;border-bottom:1px solid var(--line);position:relative}
.post:last-child{border-bottom:none}
.post-title{height:48px;background:linear-gradient(#fff,#eeeff1);color:var(--blue-title);font-size:15px;padding:14px 17px}
.bubble{position:absolute;right:38px;top:6px;width:44px;height:30px;background:#e4e6e9;border-radius:4px;font-size:12px;color:var(--blue-title);text-align:center;line-height:30px}
.thumb{position:absolute;left:22px;top:69px;width:165px;height:102px;border:2px solid #e3e3e3;background:linear-gradient(135deg,#dfe6ee,#7d92ab)}
.excerpt{position:absolute;left:208px;top:66px;width:420px;font-size:11px;line-height:18px;color:var(--grey-text)}
.byline{position:absolute;right:18px;top:159px;font-size:12px;font-style:italic;color:var(--blue-title)}
.byline b{color:var(--red);font-weight:400}
.shares{position:absolute;left:27px;top:196px;display:flex;gap:12px;font-size:10px}
.shares span{border:1px solid #c6ccd4;padding:1px 5px;color:#3b5998;background:#f3f5f8}
.shares i{font-style:normal;border:1px solid #c6ccd4;padding:1px 4px;color:#444}
.read-more{position:absolute;right:18px;top:187px;width:184px;height:28px;border-radius:4px;background:linear-gradient(var(--btn-blue),var(--btn-blue-dark));color:#fff;font-size:11px;text-align:center;line-height:28px}
.side-box{position:absolute;left:798px;width:282px;border-radius:4px;background:linear-gradient(var(--side-blue),var(--side-blue-dark));color:#fff}
.side-box h3{font-size:17px;font-weight:600;padding:13px 22px 0}
.side-icon{position:absolute;left:14px;width:70px;height:56px;background:linear-gradient(135deg,#e8d6b0,#4a7c3a);border-radius:4px}
.side-text{position:absolute;left:96px;width:172px;font-size:15px;line-height:21px}
.pill{position:absolute;left:21px;width:240px;height:38px;border-radius:19px;background:linear-gradient(#fff,#dfe3e8);color:#666;font-size:16px;text-align:center;line-height:38px}
.links{list-style:none;position:absolute;left:15px;top:52px}
.links li{width:252px;height:35px;margin-bottom:12px;border-radius:17px;background:linear-gradient(#fbfbfb,#d9dde2);color:#556;font-size:15px;line-height:35px;padding-left:15px}
.sponsors{position:absolute;left:798px;top:1410px;width:282px;height:187px;background:#efefef;border-radius:4px}
.sponsors h3{color:#3f83c2;font-size:17px;font-weight:600;padding:16px 22px}
.sponsor-grid{display:grid;grid-template-columns:1fr 1fr;row-gap:34px;padding:2px 20px;font-size:17px;font-weight:700;color:#1c3e7a;text-align:center}
.advert{position:absolute;left:798px;top:1610px;width:282px;height:233px;background:#f3f3f3}
.advert-art{position:absolute;left:50px;top:18px;width:182px;height:200px;border-radius:6px;background:linear-gradient(#d9d9d9,#e9c9c9)}
.news-field{position:absolute;left:22px;top:158px;width:240px;height:34px;background:#fff;border:1px solid #ccd;color:#888;font-size:13px;font-style:italic;padding:8px 10px}
.footer{position:absolute;right:123px;top:2352px;font-size:12px;color:#222}
</style>
</head>
<body>
<nav class="topbar"><ul><li>Home</li><li>Advertise</li><li>Contact</li></ul></nav>
<div class="page"></div>

<header>
  <div class="brand"><span class="brand-dot"></span><span class="brand-name">Velmar Quest Hub</span></div>
  <div class="social-proof">Join a Community of <span class="count">4279</span> Awesome Readers</div>
  <div class="social"><span></span><span></span><span></span><span></span><span></span></div>
</header>

<nav class="nav"><span>Articles and Videos</span><span>Trading Philosophy</span><span>Learning Centre</span><span>Free Tools</span><span>Members Only</span><span>Work With Us</span><span>About</span></nav>

<section class="hero">
  <div class="hero-screen" role="img" aria-label="Desktop monitor showing a trader at work"></div>
  <div class="dots"><span></span><span></span><span></span><span></span></div>
  <h2>DO YOU WANT TO KNOW THE TRUTH ABOUT IRON CONDORS?</h2>
  <ul>
    <li><svg width="18" height="16"><path d="M2 8l5 5 9-11" stroke="#b9cbe6" stroke-width="3" fill="none"/></svg>Learn How To Trade This Amazing Option Income Strategy With My FREE Ebook</li>
    <li><svg width="18" height="16"><path d="M2 8l5 5 9-11" stroke="#b9cbe6" stroke-width="3" fill="none"/></svg>I will share with you my blueprint and all my tips and tricks for generating consistent monthly income with iron condors</li>
  </ul>
  <div class="ebook" role="img" aria-label="3D cover of the free ebook No-Fluff Manual for Calendar Spreads"></div>
  <div class="instant">INSTANT ACCESS</div>
</section>

<h1 class="tagline">HELPING YOU TRADE IRON CONDORS AND OTHER INCOME<br>STRATEGIES WITHOUT THE BS</h1>

<h2 class="section-head" style="top:738px">LATEST POSTS</h2>
<div class="post-list" style="top:795px">
  <article class="post"><div class="post-title">LOREM IPSUM IS SIMPLY DUMMY TEXT OF THE PRINTING</div><div class="bubble">12</div><div class="thumb" role="img" aria-label="Figures climbing a rising bar chart"></div><p class="excerpt">Lorem Ipsum is simply dummy text of the printing and typesetting industry. Lorem Ipsum has been the industry's standard dummy text ever since the 1500s, when an unknown printer took a galley of type and scrambled it to make a type specimen book. It has survived not only five centuries, but also the leap into electronic typesetting, remaining essentially unchanged.</p><p class="byline">Posted by <b>Corin Waldmere</b></p><div class="shares"><span>Like</span><i>27</i><span>Tweet</span><i>129</i></div><div class="read-more">CLICK HERE TO READ MORE</div></article>
  <article class="post"><div class="post-title">LOREM IPSUM IS SIMPLY DUMMY TEXT OF THE PRINTING</div><div class="bubble">12</div><div class="thumb" role="img" aria-label="Business team in an office"></div><p class="excerpt">Lorem Ipsum is simply dummy text of the printing and typesetting industry. Lorem Ipsum has been the industry's standard dummy text ever since the 1500s, when an unknown printer took a galley of type and scrambled it to make a type specimen book. It has survived not only five centuries, but also the leap into electronic typesetting, remaining essentially unchanged.</p><p class="byline">Posted by <b>Corin Waldmere</b></p><div class="shares"><span>Like</span><i>27</i><span>Tweet</span><i>129</i></div><div class="read-more">CLICK HERE TO READ MORE</div></article>
  <article class="post"><div class="post-title">LOREM IPSUM IS SIMPLY DUMMY TEXT OF THE PRINTING</div><div class="bubble">12</div><div class="thumb" role="img" aria-label="Businessman drawing a rising line graph"></div><p class="excerpt">Lorem Ipsum is simply dummy text of the printing and typesetting industry. Lorem Ipsum has been the industry's standard dummy text ever since the 1500s, when an unknown printer took a galley of type and scrambled it to make a type specimen book. It has survived not only five centuries, but also the leap into electronic typesetting, remaining essentially unchanged.</p><p class="byline">Posted by <b>Corin Waldmere</b></p><div class="shares"><span>Like</span><i>27</i><span>Tweet</span><i>129</i></div><div class="read-more">CLICK HERE TO READ MORE</div></article>
</div>

<h2 class="section-head" style="top:1522px">FEATURED POSTS</h2>
<div class="post-list" style="top:1578px">
  <article class="post"><div class="post-title">LOREM IPSUM IS SIMPLY DUMMY TEXT OF THE PRINTING</div><div class="bubble">12</div><div class="thumb" role="img" aria-label="Smiling businessman"></div><p class="excerpt">Lorem Ipsum is simply dummy text of the printing and typesetting industry. Lorem Ipsum has been the industry's standard dummy text ever since the 1500s, when an unknown printer took a galley of type and scrambled it to make a type specimen book. It has survived not only five centuries, but also the leap into electronic typesetting, remaining essentially unchanged.</p><p class="byline">Posted by <b>Corin Waldmere</b></p><div class="shares"><span>Like</span><i>27</i><span>Tweet</span><i>129</i></div><div class="read-more">CLICK HERE TO READ MORE</div></article>
  <article class="post"><div class="post-title">LOREM IPSUM IS SIMPLY DUMMY TEXT OF THE PRINTING</div><div class="bubble">12</div><div class="thumb" role="img" aria-label="Businessman walking past office building"></div><p class="excerpt">Lorem Ipsum is simply dummy text of the printing and typesetting industry. Lorem Ipsum has been the industry's standard dummy text ever since the 1500s, when an unknown printer took a galley of type and scrambled it to make a type specimen book. It has survived not only five centuries, but also the leap into electronic typesetting, remaining essentially unchanged.</p><p class="byline">Posted by <b>Corin Waldmere</b></p><div class="shares"><span>Like</span><i>27</i><span>Tweet</span><i>129</i></div><div class="read-more">CLICK HERE TO READ MORE</div></article>
  <article class="post"><div class="post-title">LOREM IPSUM IS SIMPLY DUMMY TEXT OF THE PRINTING</div><div class="bubble">12</div><div class="thumb" role="img" aria-label="Thoughtful businessman at a desk"></div><p class="excerpt">Lorem Ipsum is simply dummy text of the printing and typesetting industry. Lorem Ipsum has been the industry's standard dummy text ever since the 1500s, when an unknown printer took a galley of type and scrambled it to make a type specimen book. It has survived not only five centuries, but also the leap into electronic typesetting, remaining essentially unchanged.</p><p class="byline">Posted by <b>Corin Waldmere</b></p><div class="shares"><span>Like</span><i>27</i><span>Tweet</span><i>129</i></div><div class="read-more">CLICK HERE TO READ MORE</div></article>
</div>

<aside>
  <section class="side-box" style="top:738px;height:195px">
    <h3>Work with us&nbsp; One-one-one</h3>
    <div class="side-icon" style="top:76px" role="img" aria-label="Handshake"></div>
    <p class="side-text" style="top:64px">We're ready to help you achieve the success you're looking for</p>
    <div class="pill" style="top:142px">CLICK HERE &raquo;</div>
  </section>
  <section class="side-box" style="top:946px;height:196px">
    <h3>New to Options?</h3>
    <div class="side-icon" style="top:64px;background:linear-gradient(135deg,#6fbf5a,#1d3a1d)" role="img" aria-label="Stock chart on a screen"></div>
    <p class="side-text" style="top:62px">Check out our comprehensive training program</p>
    <div class="pill" style="top:143px">CLICK HERE &raquo;</div>
  </section>
  <section class="side-box" style="top:1155px;height:242px">
    <h3>Free Training</h3>
    <ul class="links"><li>&raquo;&nbsp; Volatility Tutorials</li><li>&raquo;&nbsp; Iron Condor Tutorials</li><li>&raquo;&nbsp; Income Trading Tutorials</li><li>&raquo;&nbsp; Free Tools and Resources</li></ul>
  </section>
  <section class="sponsors">
    <h3>Top Sponsors</h3>
    <div class="sponsor-grid"><span>NORVALE</span><span>BRIXTONE</span><span>Halden-Rusk</span><span>PELLMAR'S</span></div>
  </section>
  <section class="advert">
    <div class="advert-art" role="img" aria-label="Advertising banner: advertise your business here, with a target, arrow and banknote"></div>
  </section>
  <section class="side-box" style="top:1856px;height:253px">
    <h3 style="padding-top:16px;padding-left:70px">Newsletter Subscribe</h3>
    <svg style="position:absolute;left:22px;top:16px" width="34" height="24"><rect x="1" y="1" width="32" height="22" fill="#fff"/><path d="M1 1l16 12 16-12" stroke="#5f9fd3" stroke-width="2" fill="none"/></svg>
    <p style="position:absolute;left:22px;top:62px;width:245px;font-size:13px;line-height:22px">Stay up to date with Velmar Quest Hub. New articles and tutorials delivered straight to your inbox</p>
    <div class="news-field">Enter your mail ID</div>
    <div class="pill" style="top:199px;left:113px;width:150px">Let's Do This &raquo;</div>
  </section>
</aside>

<footer class="footer">&copy; 2012.www.velmarquest.com</footer>
</body>
</html>
```